Meditations CD Cover
Zielgruppe
Wir unterstützen Therapeuten ihre Praxis aufzubauen.
Aufgabenstellung
Ich wünsche einen CD Cover mit Rückseite und CD Druck, wo nicht zu esoterisch aussieht. Bitte keine Buddha, Steine, Yoga, Lotusblume!
ich hätte gerne mein Bild im Vordergrund, nicht zu prominent, klar strukturiert und nicht zu schwer, lieber mehr Platz lassen.
ich hätte gerne eine CD Jewel Cases.
Bitte eine ganz neutralle CD ohne das Grün von der Website. (licht-weg-studio.ch)
Die Meditation ist eine Mischung zwischen Business und Meditation, es geht um Kundenfindung.
Etwas schlichtes und modernes.
Was rauf muss:
CD Cover
Doria Pfannstiel-Kuhmer
Mein Foto
Titel:
Finde Deinen Auftrag, Pfad des Einklangs!
bitte auch schreiben: die ÜBUNGS-CD zum Buch
Logo und mein Bild, nicht zu prominent!!!!
Beispiel: http://marenbextolli.com/
http://www.bildquellhaus.com/vector/electric-bulb-48201937?st=7302846
http://www.bildquellhaus.com/vector/dart-board-48202541?st=913ab27
http://wolkenklang-audio.com/hagen-lutz-deine-reise-zu-glanz-reichtum-und-freude-cd
Rückseite:
mein Foto und der Text:
Gehen Sie in die Resonanz und finden Sie den richtigen Klienten.
Gerne unterstütze ich Sie auf diesem wundervollen Weg ...
Mein Name ist Doria Pfannstiel, ich bin erfolgreiche Unternehmerin, die zugleich spiri- tuell denkt und handelt. Und ich bin fest davon überzeugt. Es gibt eine innere Kraft, die nicht nur Berge versetzt. Sondern auch Ihre Praxis fullt.
Auf dieser CD werden Sie angeleitet sich mit ihrem Idealkunden zu treffen. Sie werden entdecken welche Probleme oder Herausforderungen, Wünsche und Ziele Ihr potenzieller Klient.
Vielen Dank und viel Spass :-)

```html
<!DOCTYPE html>
<html lang="de">
<head>
<meta charset="utf-8">
<title>Pfad des Einklangs – CD Cover</title>
<link rel="stylesheet" href="https://fonts.googleapis.com/css2?family=Didact+Gothic&family=Montserrat:wght@600;700&family=Poiret+One&display=swap">
<style>
  :root {
    --teal: #1a8e9c;
    --teal-dark: #137884;
    --leaf-green: #2e8a4e;
    --leaf-teal: #3aa9a6;
    --leaf-light: #6cc1b8;
    --paper: #ffffff;
    --band: rgba(240, 244, 240, 0.82);
    --photo-warm: #e9dcb8;
    --photo-dark: #4a3a5c;
    --text-white: #ffffff;
    --logo-grey: #555555;
  }
  * { box-sizing: border-box; margin: 0; padding: 0; }
  html, body {
    width: 1200px; height: 520px; overflow: hidden;
    background: var(--paper);
  }
  .canvas { position: relative; width: 1200px; height: 520px; }

  /* Back cover */
  .back-cover {
    position: absolute; left: 43px; top: 0; width: 624px; height: 480px;
    background: var(--paper);
    box-shadow: 3px 4px 6px rgba(0,0,0,0.35);
    overflow: hidden;
  }
  .back-leaves {
    position: absolute; left: 150px; top: 30px; width: 440px; height: 340px;
    background: radial-gradient(ellipse at 45% 40%, rgba(214,226,170,0.45), rgba(190,222,214,0.3) 55%, rgba(255,255,255,0) 75%);
  }
  .back-text {
    position: absolute; left: 84px; top: 47px; width: 300px;
    font-family: "Didact Gothic", sans-serif; font-size: 13.4px; line-height: 16.1px;
    color: var(--teal);
  }
  .back-text p { margin-bottom: 16px; }
  .back-text .closing { margin-top: 34px; }
  .spine {
    position: absolute; top: 240px;
    font-family: "Montserrat", sans-serif; font-weight: 700; font-size: 10.5px;
    color: var(--teal); white-space: nowrap;
  }
  .spine-left { left: 15px; transform: translate(-50%, -50%) rotate(-90deg); margin-left: 6px; }
  .spine-right { left: 608px; transform: translate(-50%, -50%) rotate(90deg); margin-left: 6px; }
  .back-portrait {
    position: absolute; left: 329px; top: 259px; width: 242px; height: 221px;
    background: linear-gradient(180deg, var(--photo-dark) 0%, #8a7a7a 35%, var(--photo-warm) 70%);
    border-radius: 45% 45% 0 0;
  }
  .brand {
    position: absolute;
    font-family: "Didact Gothic", sans-serif; font-size: 15px;
    color: var(--logo-grey); display: flex; align-items: center; gap: 6px; white-space: nowrap;
  }
  .brand .dot { width: 14px; height: 14px; border-radius: 50%; background: var(--teal); }
  .back-brand { left: 84px; top: 425px; }

  /* Front cover */
  .front-cover {
    position: absolute; left: 693px; top: 0; width: 480px; height: 480px;
    box-shadow: 3px 4px 6px rgba(0,0,0,0.35);
    overflow: hidden;
  }
  .front-leaves {
    position: absolute; inset: 0;
    background: linear-gradient(160deg, var(--leaf-green) 0%, var(--leaf-teal) 55%, var(--leaf-light) 100%);
  }
  .title-band {
    position: absolute; left: 0; top: 140px; width: 480px; height: 200px;
    background: var(--band);
  }
  .front-portrait {
    position: absolute; left: 22px; top: 235px; width: 105px; height: 105px;
    background: linear-gradient(180deg, var(--photo-dark) 0%, #9a8a86 40%, var(--photo-warm) 75%);
    border-radius: 45% 45% 0 0;
  }
  .title {
    position: absolute; left: 60px; top: 160px; width: 420px; text-align: center;
    font-family: "Poiret One", sans-serif; font-size: 41px; line-height: 50px;
    color: var(--teal-dark); text-transform: uppercase; letter-spacing: -1px;
    -webkit-text-stroke: 0.8px var(--teal-dark);
  }
  .front-author {
    position: absolute; left: 130px; top: 270px; width: 280px; text-align: center;
    font-family: "Montserrat", sans-serif; font-weight: 700; font-size: 15.5px;
    color: var(--teal);
  }
  .subtitle {
    position: absolute; left: 274px; top: 392px;
    font-family: "Montserrat", sans-serif; font-weight: 700; font-size: 19px; line-height: 27px;
    color: var(--text-white); transform: rotate(-8deg); transform-origin: left top;
  }
  .front-brand { left: 24px; top: 432px; color: var(--text-white); }
  .front-brand .dot { background: var(--text-white); }
</style>
</head>
<body>
<div class="canvas">
  <section class="back-cover">
    <div class="back-leaves" role="img" aria-label="Zarte transparente Blattskelette in Gelbgrün und Türkis"></div>
    <div class="spine spine-left">Doria Pfannstiel-Kuhmer</div>
    <div class="back-text">
      <p>Gehen Sie in die Resonanz und<br>finden Sie den richtigen Klienten.<br>Gerne unterstütze ich Sie auf<br>diesem wundervollen Weg.</p>
      <p>Mein Name ist Doria Pfannstiel, ich<br>bin erfolgreiche Unternehmerin, die<br>zugleich spirituell denkt und handelt.<br>Und ich bin fest davon überzeugt.<br>Es gibt eine innere Kraft, die nicht<br>nur Berge versetzt. Sondern auch<br>Ihre Praxis füllt.</p>
      <p>Auf dieser CD werden Sie angeleitet<br>sich mit ihrem Idealkunden zu treffen.<br>Sie werden entdecken welche Probleme<br>oder Herausforderungen, Wünsche und<br>Ziele Ihr potenzieller Klient.</p>
      <p class="closing">Vielen Dank und viel Spass</p>
    </div>
    <div class="back-portrait" role="img" aria-label="Porträtfoto der Autorin in heller Bluse, getönt"></div>
    <div class="brand back-brand"><span class="dot"></span>KVL Online Marketing</div>
    <div class="spine spine-right">Doria Pfannstiel-Kuhmer</div>
  </section>

  <section class="front-cover">
    <div class="front-leaves" role="img" aria-label="Nahaufnahme grüner Blattadern im Verlauf von Grün zu Türkis"></div>
    <div class="title-band"></div>
    <div class="front-portrait" role="img" aria-label="Kleines Porträtfoto der Autorin"></div>
    <h1 class="title">Finde Deinen Auftrag,<br>Pfad des Einklangs!</h1>
    <div class="front-author">Doria Pfannstiel-Kuhmer</div>
    <div class="subtitle">die ÜBUNGS-CD<br>zum Buch</div>
    <div class="brand front-brand"><span class="dot"></span>KVL Online Marketing</div>
  </section>
</div>
</body>
</html>
```